EPIC, awesome, creative business card needed - get involved!

I'm launching a boutique, exclusive Property Management real estate agency in Sydney early next year.
The name of the agency will be called "Quartz Hill Lane" - it's a play on "chase the silver pebble trail" to wealth. The Quartz Hill Lane signifies wealth through property investment.
My business will offer management of investment properties (ie Property Management).
The difference with Quartz Hill Lane and other agencies is the business will be run by one of Australia's leading property investment experts, and also one of Australia's leading property managers.
It will be exclusively for high net worth properties and individuals, so the business card needs to be extremely sharp, slick and relatively simple.
The information I want on the card is as follows
Nolan Pryce - Director
M: 0412 967 154
P: 9735 6021
E: nolan@quartzhilllane.net.au
W: quartzhilllane.net.au
I'm happy with the red from the logo, black - no yellows or funky colors. I want this to be a super corporate and slick business card to match the high end nature of the business.
Good luck everyone, and please ask questions for clarification.

```html
<!DOCTYPE html>
<html lang="en">
<head>
<meta charset="utf-8">
<title>Quartz Hill Lane – Business Card</title>
<link rel="stylesheet" href="https://fonts.googleapis.com/css2?family=Exo+2:wght@300;400&display=swap">
<style>
  :root {
    --brand-red: #c8080c;
    --brand-deep: #8e1212;
    --panel-start: #d10a0a;
    --panel-end: #e84800;
    --frame-top: #f4846c;
    --frame-bottom: #e8000c;
    --paper: #ffffff;
    --rule: rgba(255,255,255,0.14);
    --map-tone: #f19a80;
  }
  html, body {
    margin: 0;
    width: 1200px;
    height: 1000px;
    overflow: hidden;
    background: var(--paper);
    font-family: "Exo 2", sans-serif;
  }
  .canvas { position: relative; width: 1200px; height: 1000px; }

  .card-front {
    position: absolute; left: 188px; top: 143px;
    width: 558px; height: 320px;
    background: var(--paper);
    border: 1px solid #d8d8d8;
    box-shadow: 4px 5px 6px rgba(0,0,0,0.45);
    overflow: hidden;
  }
  .brand {
    position: absolute;
    display: flex; align-items: center; gap: 22px;
  }
  .brand-dot {
    width: 84px; height: 84px; border-radius: 50%;
    background: var(--brand-red);
    flex: none;
  }
  .brand-name {
    font-weight: 300; font-size: 38px; color: var(--brand-deep);
    letter-spacing: 0.5px; white-space: nowrap;
  }
  .card-front .brand { left: 26px; top: 18px; }

  .stripe { position: absolute; left: 0; width: 100%; background: linear-gradient(90deg, var(--panel-start), var(--panel-end)); }
  .stripe-top { top: 124px; height: 13px; }
  .stripe-bottom { top: 310px; height: 10px; }

  .contact-panel {
    position: absolute; left: 0; top: 141px; width: 100%; height: 165px;
    background: linear-gradient(100deg, var(--panel-start) 25%, var(--panel-end) 100%);
  }
  .contact-list {
    position: absolute; left: 24px; top: 8px; width: 202px;
    margin: 0; padding: 0; list-style: none;
    color: #fff; font-weight: 400; font-size: 15.5px;
    border-right: 1px solid var(--rule); padding-right: 0;
    height: 156px;
  }
  .contact-list li {
    height: 31px; line-height: 31px;
    border-bottom: 1px solid var(--rule);
    white-space: nowrap;
  }
  .contact-list li:last-child { border-bottom: none; }
  .map-area {
    position: absolute; left: 374px; top: 14px; width: 156px; height: 142px;
    background: radial-gradient(ellipse at center, var(--map-tone) 55%, rgba(241,154,128,0) 72%);
    opacity: 0.9;
  }

  .card-back {
    position: absolute; left: 456px; top: 539px;
    width: 555px; height: 317px;
    box-sizing: border-box;
    border: 1px solid #d8d8d8;
    background: linear-gradient(180deg, var(--frame-top), var(--frame-bottom));
  }
  .card-back-inner {
    position: absolute; left: 11px; top: 11px; right: 11px; bottom: 11px;
    background: var(--paper);
  }
  .card-back .brand { left: 98px; top: 103px; }
</style>
</head>
<body>
<main class="canvas">
  <section class="card-front" aria-label="Business card front">
    <div class="brand">
      <span class="brand-dot"></span>
      <span class="brand-name">Quartz Hill Lane</span>
    </div>
    <div class="stripe stripe-top"></div>
    <div class="contact-panel">
      <ul class="contact-list">
        <li>Nolan Pryce – Director</li>
        <li>M: 0412 967 154</li>
        <li>P: 9735 6021</li>
        <li>E: nolan@quartzhilllane.net.au</li>
        <li>W: quartzhilllane.net.au</li>
      </ul>
      <div class="map-area" role="img" aria-label="Pale silhouette map of Australia"></div>
    </div>
    <div class="stripe stripe-bottom"></div>
  </section>

  <section class="card-back" aria-label="Business card back">
    <div class="card-back-inner">
      <div class="brand">
        <span class="brand-dot"></span>
        <span class="brand-name">Quartz Hill Lane</span>
      </div>
    </div>
  </section>
</main>
</body>
</html>
```